Harrowby Wine Label - Design a front and smaller back label for an exclusive red wine

Harrowby Wines produces a very high quality, high priced wine from an old and prestigous vineyard in one of Australia's oldest, but smallest wine growing regions. The grapevines are old (like old men with gnarled arms and trunks) and they produce fewer grapes than younger vines but the grape quality (and thus wine quality) is magnificent and highly sought after as it produces wine of exceptional quality.
The vineyard was purchased by the Harrowby family in February 2010 from a multinational wine company who made wonderful, trophy winning wines for 10 years before the vineyard went into a decline.
The challenge is to produce 2 labels - a simple main front label that focuses on the Harrowby brand and a smaller, information rich, back label that relates the history of the vineyard.
The labels should have a white or charcoal grey background and impart tradition, quality, exclusivity and a little self indulgence which is why we want the family crest incorporated - the choice of font will help.
It might also impart a sense of fun so that it appeals to the 25-35 year old age bracket.
The label should be kept clean and simple not loud and busy. Preferred colours are black, grey and white. Red is fine if used sparingly

Here are the details:_

Front Label (115 long x 65-90mm wide)

Harrowby
Lanternwatch Reserve
2011
Mudgee
Wine of Australia 750ml

Back Label (dimensions to suit text and front label design; font size small; text in black so that it is readable in less than optimal light (eg candlelight at a restaurant table).

Harrowby
Lanternwatch Reserve 2011

This is the first release of The Lanternwatch’s Reserve – just 100 dozen bottles were made. The wine was made from Shiraz and 10% Cabernet Sauvignon grapes sourced from an iconic Mudgee vineyard that was established 1966 by Peter Vallis. In 1994, the vineyard known as ”Silver Hollow”, became the source of a decade of formidable, trophy winning wines under Tindalberg’s and later Quellwood’s ownership. The 20ha vineyard was purchased by Corin & Margaret Harrowby in 2010. The Silver Hollow name was retained by Quellwoods; no wine has been released under this label since the 2006 vintage.

The shaky old Shiraz vines are slowly being restored to full health using careful cane pruning techniques that stimulates fresh, new tissue growth, more even bunch sizes and better grape quality and consistency. The Shiraz grapes used in this wine were hand-picked from two rows of the first crop from the 46 year old, cane pruned vines. The 2011 Reserve is the first step to re-establish the traditions of a famous vineyard and one of Australia’s most sought after export wines.

“Deep and intense purple hues with aromas of ripe blackberry fruits, spice and eucalypt with rich chocolate complemented by subtle oak overtones. A rich and full bodied wine exhibiting a soft yet generous palate with plum, forest fruits and mint chocolate notes. A fine grained tannin structure displaying integrated oak characters adds to the complexity of the wine. This wine was aged for 18 months in a blend of new French oak hogsheads and one year old American hogsheads, crafting a blend with great structure and length of flavour which will develop into a Mudgee classic” – Lewis Farrant, Winemaker

13.5% Alc/Vol.
Contains approx 8.0 std drinks
Preservative (220) added

Harrowby Wines
Tallowbend Rd, Mudgee 2850
www.harrowbywines.example.au

Reason: My apologies to the designers who have kindly submitted some wonderful designs. I am trying to achieve a conscentious between shareholders. This is difficult as they are in different parts of the world and I have learned through this experience that opinions on wine labels are quite diverse!!! The feedback I have received so far indicates the following (1) A light or white background is preferred (2) The crest should not be a dominant part of the label (3) The label needs to be clean, fresh and uncomplicated (4) If red is used it should be in minor detail only (5) "Harrowby" should be distinctive. The font is difficult for us! (6) We are considering "The Lanternwatch" RESERVE instead of "Lanternwatch's" RESERVE (7) The text on the back label is too long; I will edit and re-upload Many thanks for your help and patience Kind regards Corin

Good Morning All,
I have edited the back label text to reduce the size of the label. A Word file with the changes has just been uploaded.
Cheers
Corin

Dear Designers,
Thank you all so very much for the wonderful selection of designs you have submitted my family have all been overwhelmed by the quality and skill level exhibited and we all appreciate you your efforts
Kindest regards
Corin

Target Market(s)

25-35 year old men and women of Australia, China, US & UK

Industry/Entity Type

Restaurant

Requirements
Must have
• Crest
Should not have
• Animals on the label

```html
<!DOCTYPE html>
<html lang="en">
<head>
<meta charset="utf-8">
<title>Harrowby Wine Label</title>
<link rel="stylesheet" href="https://fonts.googleapis.com/css2?family=Federo&family=Almendra:wght@400&family=Cormorant+Garamond:wght@500&family=Cormorant+SC:wght@500&family=Arimo:wght@700&family=Open+Sans:wght@300&display=swap">
<style>
  :root {
    --page: #f4f4f4;
    --charcoal: #2b2a2c;
    --charcoal-deep: #222123;
    --ring-light: #3b3a3c;
    --ring-mid: #333234;
    --ink-light: #ececec;
    --ink-soft: #cfcfcf;
    --rose: #c8125e;
    --berry: #e0397a;
    --wine: #9e0c2c;
  }
  * { margin: 0; padding: 0; box-sizing: border-box; }
  html, body { width: 1200px; height: 849px; overflow: hidden; background: var(--page); }
  .canvas { position: relative; width: 1200px; height: 849px; }

  .label {
    position: absolute; top: 75px; width: 367px; height: 700px; overflow: hidden;
    color: var(--ink-light); text-align: center;
    background:
      radial-gradient(circle at 52% 100px, var(--charcoal-deep) 0 105px, transparent 106px),
      radial-gradient(circle at 62% 110px,
        var(--charcoal) 0 150px, var(--ring-mid) 151px 250px,
        var(--charcoal) 251px 330px, var(--ring-light) 331px 420px,
        var(--ring-mid) 421px 520px, var(--charcoal) 521px);
  }
  .label--front { left: 217px; }
  .label--back { left: 616px; }

  .crest-mark { display: flex; align-items: center; justify-content: center; gap: 5px;
    font-family: "Federo", sans-serif; font-size: 13px; letter-spacing: 2px; color: var(--ink-soft); }
  .crest-mark::before { content: ""; width: 8px; height: 8px; border-radius: 50%; background: var(--ink-soft); }

  .brand { font-family: "Federo", sans-serif; font-weight: 400; letter-spacing: 3px; color: #f3f3f3; line-height: 1; }
  .reserve { font-family: "Almendra", serif; color: var(--rose); line-height: 1; }
  .vintage { font-family: "Cormorant Garamond", serif; font-weight: 500; color: #fff; line-height: 1; }
  .region { font-family: "Arimo", sans-serif; font-weight: 700; color: #fff; line-height: 1; }

  .label--front .crest-mark { position: absolute; top: 205px; left: 0; right: 0; }
  .label--front .brand { position: absolute; top: 290px; left: 0; right: 0; font-size: 52px; }
  .label--front .reserve { position: absolute; top: 378px; left: 0; right: 0; font-size: 28px; }
  .label--front .vintage { position: absolute; top: 418px; left: 0; right: 0; font-size: 42px; }
  .label--front .region { position: absolute; top: 462px; left: 0; right: 0; font-size: 21px; }

  .stem { position: absolute; left: 50%; width: 1px; background: var(--ink-soft); }
  .label--front .stem { top: 492px; height: 70px; }

  .grape-motif {
    position: absolute; left: 0; right: 0; bottom: 0;
    background: linear-gradient(170deg, var(--berry) 0%, var(--rose) 45%, var(--wine) 100%);
  }
  .label--front .grape-motif { height: 182px; border-radius: 48% 52% 0 0 / 30% 40% 0 0; }
  .label--back .grape-motif { height: 46px; left: 200px; border-radius: 60% 40% 0 0 / 80% 70% 0 0; }

  .footer-line { position: absolute; left: 0; right: 0; bottom: 30px;
    font-family: "Almendra", serif; font-size: 16px; color: #fff; }

  .label--back .crest-mark { position: absolute; top: 30px; left: 0; right: 0; font-size: 10px; }
  .label--back .brand { position: absolute; top: 64px; left: 0; right: 0; font-size: 44px; letter-spacing: 2px; }
  .label--back .reserve { position: absolute; top: 115px; left: 0; right: 0; font-size: 16px; }
  .label--back .vintage { position: absolute; top: 138px; left: 0; right: 0; font-size: 22px; }

  .story { position: absolute; top: 205px; left: 26px; right: 26px;
    font-family: "Open Sans", sans-serif; font-weight: 300; font-size: 9.6px; line-height: 1.22; color: var(--ink-light); }
  .story p + p { margin-top: 9px; }

  .details { position: absolute; z-index: 2; top: 606px; left: 30px; right: 26px; display: flex; justify-content: space-between;
    font-family: "Cormorant SC", serif; font-weight: 500; font-size: 10.5px; line-height: 1.15; color: var(--ink-light); }
  .details__legal { text-align: left; }
  .details__maker { text-align: right; }
  .label--back .stem { top: 600px; height: 100px; left: 50%; }
</style>
</head>
<body>
<main class="canvas">

  <section class="label label--front" aria-label="Front label">
    <div class="crest-mark">Harrowby</div>
    <h1 class="brand">HARROWBY</h1>
    <p class="reserve">Lanternwatch's Reserve</p>
    <p class="vintage">2011</p>
    <p class="region">Mudgee</p>
    <span class="stem"></span>
    <div class="grape-motif" role="img" aria-label="Cluster of overlapping pink and red grape circles"></div>
    <p class="footer-line">Wine of Australia 750ml</p>
  </section>

  <section class="label label--back" aria-label="Back label">
    <div class="crest-mark">Harrowby</div>
    <h2 class="brand">HARROWBY</h2>
    <p class="reserve">Lanternwatch's Reserve</p>
    <p class="vintage">2011</p>
    <div class="story">
      <p>This is the first release of the Lanternwatch's Reserve – just 100 dozen bottles were made. The wine was made from Shiraz and 10% Cabernet Sauvignon grapes sourced from an iconic Mudgee vineyard that was established 1966 by Peter Vallis. In 1994, the vineyard known as “Silver Hollow”, became the source of a decade of formidable, trophy winning wines under Tindalberg’s and later Quellwood’s ownership. The 20ha vineyard was purchased by Corin &amp; Margaret Harrowby in 2010. The Silver Hollow name was retained by Quellwoods; no wine has been released under this label since the 2006 vintage.</p>
      <p>The shaky old Shiraz vines are slowly being restored to full health using careful cane pruning techniques that stimulates fresh, new tissue growth, more even bunch sizes and better grape quality and consistency. The Shiraz grapes used in this wine were hand-picked from two rows of the first crop from the 46 year old, cane pruned vines. The 2011 Reserve is the first step to re-establish the traditions of a famous vineyard and one of Australia’s most sought after export wines.</p>
      <p>“Deep and intense purple hues with aromas of ripe blackberry fruits, spice and eucalypt with rich chocolate complemented by subtle oak overtones. A rich and full bodied wine exhibiting a soft yet generous palate with plum, forest fruits and mint chocolate notes. A fine grained tannin structure displaying integrated oak characters adds to the complexity of the wine. This wine was aged for 18 months in a blend of new French oak hogsheads and one year old American hogsheads, crafting a blend with great structure and length of flavour which will develop into a Mudgee classic” – Lewis Farrant, Winemaker</p>
    </div>
    <span class="stem"></span>
    <div class="details">
      <p class="details__legal">13.5% Alc/Vol.<br>Contains approx 8.0 std drinks<br>Preservative (220) added</p>
      <p class="details__maker">Harrowby Wines<br>Tallowbend Rd, Mudgee 2850<br>www.harrowbywines.example.au</p>
    </div>
    <div class="grape-motif" role="img" aria-label="Small cluster of pink and red grape circles"></div>
  </section>

</main>
</body>
</html>
```